Quorvix Letter head

Quorvix is a young and energetic software development consultancy. We spend our time working with clients to turn what ever is in their heads in to software.
We are trying to create an image of a high class software boutique who build class leading bespoke solutions.
We need a sharp letter head that looks great on high quality media.
We like bold colours and distinctive design. So show us what you can do.
Industry/Entity Type
Software
Requirements
Must have
- Our company is based in the UK and are requried to have on the paper somewhere the following information:
* Registered company name: Quorvix Ltd
* Registered company number
* VAT registration number
In addition we also want the following:
* An email address
* Telephone number
* Website address
An example of what some pages have in their footer is something like the following:
Quorvix Ltd is registered in England and Wales. Reg. no: 5316274
Registered office: 48 Cobblewick Road, Harlow Essex, CM93TP. Tel: 07712365081
You do not have to use this sentance but please make sure your design incorporates accommodates the requirements for UK based companies

```html
<!DOCTYPE html>
<html lang="en">
<head>
<meta charset="utf-8">
<title>Quorvix Letterhead</title>
<link href="https://fonts.googleapis.com/css2?family=Josefin+Sans:wght@300;400&family=Open+Sans:wght@400&display=swap" rel="stylesheet">
<style>
  :root {
    --paper: #ffffff;
    --brand-red: #d0262f;
    --brand-red-soft: #eecdd1;
    --ink: #1e1e1e;
    --ink-muted: #666666;
  }
  * { margin: 0; padding: 0; box-sizing: border-box; }
  html, body { width: 886px; height: 1200px; overflow: hidden; background: var(--paper); }
  .letterhead {
    position: relative;
    width: 886px;
    height: 1200px;
    background: var(--paper);
    font-family: "Open Sans", Arial, sans-serif;
    color: var(--ink);
  }
  .margin-rule {
    position: absolute;
    top: 18px;
    bottom: 0;
    width: 5px;
    background: var(--brand-red);
  }
  .margin-rule--outer { left: 52px; }
  .margin-rule--inner { left: 59px; }
  .brand {
    position: absolute;
    left: 71px;
    top: 14px;
  }
  .brand__name {
    font-family: "Josefin Sans", Arial, sans-serif;
    font-weight: 400;
    font-size: 44px;
    letter-spacing: 1px;
    line-height: 1;
    color: var(--brand-red);
  }
  .brand__reg {
    position: absolute;
    left: 176px;
    top: 48px;
    font-size: 7px;
    color: var(--ink-muted);
    white-space: nowrap;
  }
  .registered-office {
    position: absolute;
    right: 28px;
    top: 38px;
    text-align: right;
    font-size: 12px;
    line-height: 16px;
  }
  .watermark {
    position: absolute;
    left: 122px;
    top: 530px;
  }
  .watermark text {
    font-family: "Josefin Sans", Arial, sans-serif;
    font-weight: 300;
    font-size: 148px;
    fill: var(--brand-red-soft);
  }
  .footer-rule {
    position: absolute;
    right: 0;
    width: 279px;
    height: 3px;
    background: linear-gradient(to right, rgba(208, 38, 47, 0), var(--brand-red) 70%);
  }
  .footer-rule--upper { top: 1125px; }
  .footer-rule--lower { top: 1131px; }
  .contact {
    position: absolute;
    right: 23px;
    top: 1138px;
    text-align: right;
    font-size: 20px;
    line-height: 23px;
  }
  .contact__web { margin-right: 7px; }
</style>
</head>
<body>
  <main class="letterhead">
    <div class="margin-rule margin-rule--outer"></div>
    <div class="margin-rule margin-rule--inner"></div>

    <header>
      <div class="brand">
        <div class="brand__name">QUORVIX</div>
        <div class="brand__reg">Reg.No. 5316274</div>
      </div>
      <address class="registered-office" style="font-style: normal;">
        <div>Registered Office: 48 Cobblewick Road, Harlow Essex, CM93TP.</div>
        <div>Tel No: 07712365081</div>
      </address>
    </header>

    <svg class="watermark" width="694" height="130" viewBox="0 0 694 130" aria-hidden="true">
      <text x="0" y="123" textLength="694" lengthAdjust="spacingAndGlyphs">QUORVIX</text>
    </svg>

    <div class="footer-rule footer-rule--upper"></div>
    <div class="footer-rule footer-rule--lower"></div>
    <footer class="contact">
      <div class="contact__email">info@quorvix.com</div>
      <div class="contact__web">www.quorvix.uk</div>
    </footer>
  </main>
</body>
</html>
```